Web application design for investigative software

ThreadKove is an investigation web application that would organize, create visualizations and allow collaboration. It’s available to anyone and can be used by students, historians, watchdog groups, civic hackers, investigative reporters, mystery enthusiasts, authors, even conspiracy theorists.

We are looking for two related pages. The first, a splash, or front, page and the second a ‘template’ for the web application. They should both be styled the same. The only restriction is that the logo is set.

The design should also be modern and visually well organized — employing a combination of visual devices and info graphics. Keep it light and not too heavy but strong/ professional. Do not be influenced by the current colors of threadkove.example, though the colors should be compatible with the logo..

The pages should be compatible with bootstrap, mostly for it’s JS and component functionality. It can be advised by the designer that a subset of bootstrap be used.

The splash page.
Something along the lines of (though not a copy of) :
https://www.brimloft.example/advertise
http://www.palvornhosting.example/
http://www.murkelsoft.example/
http://www.vontasky.example/

I have a very rough wire frame ish html file uploaded. Use a a guide, but alternate ideas are encouraged.

The application page should have some sort of bar for at the top for system level links a header and a footer. A vertical column to the left between the header and footer for ads, though this will be dynamic as a user can pay out of seeing adds. All dynamic actions will be made by the developers at ThreadKove.

WARNING. Please do not submit pre-made templates from some template website. We can do that ourselves for free.

This project will deliver CODE. HTML, CSS and supporting graphics and files.

```html
<!DOCTYPE html>
<html lang="en">
<head>
<meta charset="utf-8">
<title>ThreadKove — Track, Relate, Investigate, Solve</title>
<link rel="stylesheet" href="https://fonts.googleapis.com/css2?family=Questrial&family=Open+Sans:wght@400;600&display=swap">
<style>
:root{
  --red:#c0201f;
  --red-dark:#a71c1b;
  --red-deep:#8f1615;
  --ink:#2b2b2b;
  --text:#555;
  --muted:#888;
  --rule:#d8d8d8;
  --paper:#fff;
  --mist:#efefef;
  --bar:#2d2d2d;
}
*{box-sizing:border-box;margin:0;padding:0}
html,body{width:1200px;height:2535px;overflow:hidden}
body{position:relative;background:var(--paper);font-family:"Open Sans",Arial,sans-serif;color:var(--text)}
a{color:inherit;text-decoration:none}
.abs{position:absolute}

/* top bar */
.topbar{left:0;top:0;width:1200px;height:37px;background:var(--bar);color:#ddd;font-size:13px}
.topbar .contact{left:152px;top:10px;display:flex;gap:28px;align-items:center}
.topbar .contact span{display:flex;align-items:center;gap:8px}
.topbar .btn{top:5px;height:27px;line-height:27px;text-align:center;font-size:13px;color:#fff}
.btn-signin{left:874px;width:87px;background:var(--red)}
.btn-signup{left:966px;width:87px;background:#666}

/* header */
.header{left:0;top:37px;width:1200px;height:137px;background:#fff}
.brand{left:152px;top:38px;display:flex;align-items:center;gap:12px}
.brand-dot{width:52px;height:52px;border-radius:50%;background:var(--red)}
.brand-name{font-family:"Open Sans",sans-serif;font-weight:600;font-size:30px;color:var(--ink)}
.nav{top:63px;font-family:"Questrial",sans-serif;font-size:13px;letter-spacing:1px;color:#333}
.nav.active{color:var(--red)}
.header-rule{left:0;top:174px;width:1200px;height:9px;background:linear-gradient(#d0d0d0,#b8b8b8)}

/* hero */
.hero{left:0;top:183px;width:1200px;height:434px;background:linear-gradient(#2a2a2a,#444 40%,#1e1e1e)}
.hero-band{left:0;top:337px;width:1200px;height:97px;background:linear-gradient(var(--red),var(--red-dark))}
.hero-title{left:0;top:68px;width:1200px;text-align:center;font-family:"Questrial",sans-serif;font-weight:400;font-size:38px;letter-spacing:2px;color:#fff}
.hero-title em{font-style:normal;color:var(--red)}
.hero-devices{left:355px;top:172px;width:507px;height:235px;border-radius:6px;background:linear-gradient(#f4f4f4,#cfd4d8 60%,#8c9298)}

/* feature cards */
.card{left:142px;width:284px;height:137px;background:#fff;box-shadow:0 1px 5px rgba(0,0,0,.25);border-bottom:4px solid var(--red)}
.card.dark{border-bottom-color:#111}
.card svg{position:absolute;left:14px;top:36px}
.card h3{position:absolute;left:90px;top:16px;font-family:"Questrial",sans-serif;font-weight:400;font-size:16px;letter-spacing:1px;color:#222}
.card p{position:absolute;left:90px;top:42px;width:182px;height:60px;overflow:hidden;font-size:11.5px;line-height:15px;color:#666}
.card .more{position:absolute;left:90px;top:108px;font-size:11.5px;color:var(--red)}

.welcome-title{left:512px;top:684px;font-family:"Questrial",sans-serif;font-weight:400;font-size:31px;letter-spacing:1px;color:#444;display:flex;align-items:center;gap:10px}
.welcome-title b{font-weight:400;color:var(--red)}
.welcome-title i{display:inline-block;width:22px;height:22px;border-radius:50%;background:var(--red)}
.welcome-rule{left:508px;top:738px;width:526px;height:1px;background:var(--rule)}
.welcome-copy{left:514px;top:756px;width:518px;font-size:12.6px;line-height:18.6px;color:#555;hyphens:auto}
.welcome-copy p{margin-bottom:18px}

/* how it works */
.how{left:0;top:1183px;width:1200px;height:567px;background:linear-gradient(160deg,#f3f3f3 0%,#ececec 60%,#dedede 100%);border-top:1px solid #ddd}
.how-title{left:0;top:32px;width:1200px;text-align:center;font-family:"Questrial",sans-serif;font-weight:400;font-size:31px;letter-spacing:1px;color:#444}
.how-title b{font-weight:400;color:var(--red)}
.how-rule{left:138px;top:87px;width:918px;height:1px;background:var(--rule)}
.step{width:430px;height:80px}
.step .icon{position:absolute;left:0;top:0;width:78px;height:68px;background:linear-gradient(#fafafa,#e6e6e6);border:1px solid #ddd;box-shadow:0 2px 3px rgba(0,0,0,.15);display:flex;align-items:center;justify-content:center}
.step h4{position:absolute;left:107px;top:0;font-weight:400;font-size:13.5px;letter-spacing:.3px;color:var(--red);text-transform:uppercase}
.step p{position:absolute;left:107px;top:20px;width:282px;font-size:13px;line-height:18.6px;color:#555}
.more-btn{left:504px;top:488px;width:160px;height:38px;background:linear-gradient(var(--red),var(--red-deep));border-radius:2px;color:#fff;font-size:12.5px;letter-spacing:.5px;box-shadow:0 2px 4px rgba(0,0,0,.3)}
.more-btn span{position:absolute;left:20px;top:11px}
.more-btn i{position:absolute;right:0;top:0;width:38px;height:38px;border-left:1px solid rgba(0,0,0,.25);display:flex;align-items:center;justify-content:center}

/* what do I get */
.get{left:0;top:1750px;width:1200px;height:427px;background:var(--mist)}
.get-title{left:162px;top:57px;font-family:"Questrial",sans-serif;font-weight:400;font-size:31px;letter-spacing:1px;color:#444}
.get-title b{font-weight:400;color:var(--red)}
.get-rule{left:162px;top:113px;width:860px;height:1px;background:#cfcfcf}
.get-copy{left:171px;top:144px;width:445px;font-size:12.6px;line-height:18.6px;color:#555;hyphens:auto}
.get-copy p{margin-bottom:18px}
.get-photo{left:684px;top:143px;width:322px;height:284px;border-radius:120px 120px 0 0;background:linear-gradient(#e4e6ea,#8fa3bf 55%,#5e7596)}

/* footer */
.footer{left:0;top:2177px;width:1200px;height:321px;background:var(--red)}
.footer-band{left:0;top:0;width:1200px;height:51px;background:var(--red-dark)}
.fcol{top:85px;width:200px}
.fcol h5{font-family:"Questrial",sans-serif;font-weight:400;font-size:15px;letter-spacing:1px;color:#fff;margin-bottom:38px}
.fcol ul{list-style:none}
.fcol li{font-size:12.5px;letter-spacing:.5px;color:#fff;height:29.6px;line-height:22px;border-bottom:1px solid rgba(255,255,255,.15);width:150px}
.fcol li::before{content:"› ";font-weight:600}
.fcol .line{font-size:12.5px;color:#fff;display:flex;gap:10px;align-items:center;margin-bottom:8px}
.socials{display:flex;gap:8px;margin-top:12px}
.socials span{width:21px;height:21px;border-radius:50%;background:#fff}
.news p{font-size:11.5px;color:#fff;margin:-4px 0 8px}
.news form{display:flex}
.news input{width:110px;height:26px;border:0;padding:0 6px;font:12px "Open Sans",sans-serif}
.news button{width:47px;height:26px;border:0;background:#2b2b2b;color:#fff;font:11px "Open Sans",sans-serif}

.bottombar{left:0;top:2498px;width:1200px;height:37px;background:var(--bar);color:#ddd;font-size:11px}
.bottombar .copy{left:199px;top:12px}
.bottombar .links{left:848px;top:12px}
</style>
</head>
<body>

<div class="abs topbar">
  <div class="abs contact">
    <span><svg width="16" height="12" viewBox="0 0 16 12"><path d="M1 4c0-3 14-3 14 0v2h-4V4H5v2H1z" fill="#ddd"/><rect x="3" y="6" width="10" height="6" rx="1" fill="#ddd"/></svg>02-5550-173 or 11-5550-284</span>
    <span><svg width="14" height="10" viewBox="0 0 14 10"><rect width="14" height="10" fill="#ddd"/><path d="M0 0l7 6 7-6" stroke="#2d2d2d" fill="none"/></svg>office@threadkove.example</span>
  </div>
  <a class="abs btn btn-signin" href="#">Sign In</a>
  <a class="abs btn btn-signup" href="#">Sign Up</a>
</div>

<header class="abs header">
  <a class="abs brand" href="#"><span class="brand-dot"></span><span class="brand-name">ThreadKove</span></a>
  <a class="abs nav active" href="#" style="left:451px">HOME</a>
  <a class="abs nav" href="#" style="left:561px">WHAT IS THREADKOVE</a>
  <a class="abs nav" href="#" style="left:762px">HOW IT WORKS</a>
  <a class="abs nav" href="#" style="left:931px">GET THE SOFTWARE</a>
</header>
<div class="abs header-rule"></div>

<section class="abs hero" role="img" aria-label="Blurred photo of people in a meeting room">
  <div class="abs hero-band"></div>
  <h1 class="abs hero-title">Track, <em>Relate,</em> Investigate, <em>Solve</em></h1>
  <div class="abs hero-devices" role="img" aria-label="Tablet, laptop and phone showing the ThreadKove dashboard with line charts"></div>
</section>

<article class="abs card" style="top:673px">
  <svg width="62" height="56" viewBox="0 0 62 56"><path d="M31 2l29 14-29 14L2 16z" fill="var(--red)"/><path d="M2 26l29 14 29-14M2 36l29 14 29-14" stroke="#111" stroke-width="5" fill="none"/></svg>
  <h3>ORGANIZE</h3>
  <p>ThreadKove is an on-line system that allows you to enter what you know about a person, event, object, or group. Who</p>
  <a class="more" href="#">Read more »</a>
</article>
<article class="abs card dark" style="top:823px">
  <svg width="62" height="56" viewBox="0 0 62 56"><path d="M2 28C16 8 46 8 60 28 46 48 16 48 2 28z" fill="#111"/><circle cx="31" cy="28" r="12" fill="#fff"/><circle cx="31" cy="28" r="7" fill="var(--red)"/></svg>
  <h3>VISUALIZE</h3>
  <p>Once data has been entered, use ThreadKove's graphical analysis tools to analyze your data in new ways.</p>
  <a class="more" href="#">Read more »</a>
</article>
<article class="abs card" style="top:974px">
  <svg width="62" height="56" viewBox="0 0 62 56"><circle cx="12" cy="12" r="6" fill="var(--red)"/><circle cx="50" cy="12" r="6" fill="var(--red)"/><circle cx="31" cy="9" r="7" fill="#111"/><rect x="4" y="20" width="16" height="26" rx="3" fill="var(--red)"/><rect x="42" y="20" width="16" height="26" rx="3" fill="var(--red)"/><rect x="22" y="18" width="18" height="34" rx="3" fill="#111"/></svg>
  <h3>COLLABORATE</h3>
  <p>Join with others. Lorem ipsum dolor sit amet, consectetur adipiscing elit. Maecenas quis erat sodales, consequat nunc</p>
  <a class="more" href="#">Read more »</a>
</article>

<h2 class="abs welcome-title">Welcome to <b>ThreadKove</b><i></i></h2>
<div class="abs welcome-rule"></div>
<div class="abs welcome-copy">
  <p>Have you ever compiled a lot of data about something, but been unable to figure out what it means? Often, the number of people involved, the number of events at which they might have met, and the number of common contacts are just too much for a person to track. This can happen when you are trying to understand the players and interests in current events, or the characters and actions in a novel. It's easy to collect the data, but hard to visualize it or analyze the relationships.</p>
  <p>This is where ThreadKove comes in. ThreadKove allows you to easily visualize people, events, things, groups, and timelines and to easily see the relationships between them.</p>
  <p>Use ThreadKove to plot a novel, or to investigate a crime. Use it to analyze your favorite conspiracy theory and look for relationships that have eluded the investigators. Use it to track the causes and results of historical events – or current ones. Use it to track changing relationships among your friends at high school. Use it to track the twists and turns of a role-playing game. There's no end to what you can investigate with ThreadKove</p>
</div>

<section class="abs how">
  <h2 class="abs how-title">How <b>it works?</b></h2>
  <div class="abs how-rule"></div>

  <div class="abs step" style="left:177px;top:146px">
    <div class="icon"><svg width="34" height="30" viewBox="0 0 34 30"><rect x="2" y="16" width="8" height="14" fill="var(--red)"/><rect x="13" y="8" width="8" height="22" fill="var(--red)"/><rect x="24" y="0" width="8" height="30" fill="var(--red)"/></svg></div>
    <h4>Use graphical analysis</h4>
    <p>Use ThreadKove's graphical analysis tools to analyze your data in new ways.</p>
  </div>
  <div class="abs step" style="left:177px;top:248px">
    <div class="icon"><svg width="32" height="32" viewBox="0 0 32 32"><circle cx="13" cy="13" r="9" stroke="var(--red)" stroke-width="4" fill="none"/><path d="M20 20l9 9" stroke="var(--red)" stroke-width="5"/></svg></div>
    <h4>Use relationship maps</h4>
    <p>Use relationship maps to find out how two people or groups are associated.</p>
  </div>
  <div class="abs step" style="left:177px;top:348px">
    <div class="icon"><svg width="32" height="34" viewBox="0 0 32 34"><circle cx="16" cy="19" r="12" stroke="var(--red)" stroke-width="4" fill="none"/><rect x="12" y="1" width="8" height="4" fill="var(--red)"/><path d="M16 19l5-6" stroke="var(--red)" stroke-width="3"/></svg></div>
    <h4>Use timeline analysis</h4>
    <p>Use timeline analysis to show cause and effect of seemingly unrelated events.</p>
  </div>

  <div class="abs step" style="left:657px;top:146px">
    <div class="icon"><svg width="34" height="34" viewBox="0 0 34 34"><g stroke="var(--red)" stroke-width="2"><path d="M17 17L17 4M17 17L29 11M17 17L27 27M17 17L7 27M17 17L5 11"/></g><circle cx="17" cy="17" r="6" fill="var(--red)"/><g fill="var(--red)"><circle cx="17" cy="4" r="3"/><circle cx="29" cy="11" r="3"/><circle cx="27" cy="27" r="3"/><circle cx="7" cy="27" r="3"/><circle cx="5" cy="11" r="3"/></g></svg></div>
    <h4>Use social network mapping</h4>
    <p>Use social network mapping to show how relationships change over time.</p>
  </div>
  <div class="abs step" style="left:657px;top:248px">
    <div class="icon"><svg width="32" height="32" viewBox="0 0 32 32"><rect x="2" y="5" width="28" height="25" stroke="var(--red)" stroke-width="3" fill="none"/><rect x="2" y="5" width="28" height="6" fill="var(--red)"/><g fill="var(--red)"><rect x="7" y="15" width="4" height="4"/><rect x="14" y="15" width="4" height="4"/><rect x="21" y="15" width="4" height="4"/><rect x="7" y="22" width="4" height="4"/><rect x="14" y="22" width="4" height="4"/><rect x="21" y="22" width="4" height="4"/></g></svg></div>
    <h4>Look for events or relationships</h4>
    <p>Look for events that stand out or relationships that have great impact on multiple events.</p>
  </div>
  <div class="abs step" style="left:657px;top:348px">
    <div class="icon"><svg width="36" height="36" viewBox="0 0 36 36"><g stroke="var(--red)" stroke-width="1.6" fill="none"><path d="M18 2v32M2 18h32M6 6l24 24M30 6L6 30"/><circle cx="18" cy="18" r="5"/><circle cx="18" cy="18" r="10"/><circle cx="18" cy="18" r="15"/></g></svg></div>
    <h4>Look for intersections</h4>
    <p>Like a spider's web, look for the intersections that matter, then look for the players that brought that intersection into focus.</p>
  </div>

  <a class="abs more-btn" href="#"><span>MORE DETAILS</span><i><svg width="16" height="14" viewBox="0 0 16 14"><path d="M1 7h9M7 3l4 4-4 4" stroke="#fff" stroke-width="2" fill="none"/><path d="M13 1h2v12h-2" stroke="#fff" stroke-width="2" fill="none"/></svg></i></a>
</section>

<section class="abs get">
  <h2 class="abs get-title">What do I get with <b>ThreadKove?</b></h2>
  <div class="abs get-rule"></div>
  <div class="abs get-copy">
    <p>Basic ThreadKove will allow any registered user to create, maintain and analyze one investigation. Advanced features will be available a la carte and will include special analytical reports, multiple investigations, and the ability to share an investigation among multiple users. Investigations of general interest could also be shared publicly in read-only mode.</p>
    <p>You will also get access to several read-only public investigations to use as a model. These might include the plots of popular novels or movies, the details of a major political event, or an investigation into a famous crime.</p>
  </div>
  <div class="abs get-photo" role="img" aria-label="Photo of a smiling man in a blue shirt holding an open laptop"></div>
</section>

<footer class="abs footer">
  <div class="abs footer-band"></div>
  <div class="abs fcol" style="left:201px">
    <h5>Product Info</h5>
    <ul><li>Sublink here</li><li>Sublink here</li><li>Sublink here</li><li>Sublink here</li></ul>
  </div>
  <div class="abs fcol" style="left:411px">
    <h5>Additional Info</h5>
    <ul><li>F.A.Q</li><li>Terms &amp; Usage</li><li>Privacy Policy</li><li>Sitemap</li></ul>
  </div>
  <div class="abs fcol" style="left:638px;width:220px">
    <h5>Contact us</h5>
    <div class="line"><svg width="14" height="10" viewBox="0 0 14 10"><rect width="14" height="10" fill="#fff"/><path d="M0 0l7 6 7-6" stroke="var(--red)" fill="none"/></svg>office@threadkove.example</div>
    <div class="line"><svg width="14" height="11" viewBox="0 0 16 12"><path d="M1 4c0-3 14-3 14 0v2h-4V4H5v2H1z" fill="#fff"/><rect x="3" y="6" width="10" height="6" rx="1" fill="#fff"/></svg>02-5550-173</div>
    <div class="socials"><span></span><span></span><span></span></div>
  </div>
  <div class="abs fcol news" style="left:859px">
    <h5>Newsletter Signup</h5>
    <p>Subscribe to get updates</p>
    <form><input type="email" placeholder="Email address"><button type="button">SEND</button></form>
  </div>
</footer>

<div class="abs bottombar">
  <span class="abs copy">Copyright © 2014 ThreadKove</span>
  <span class="abs links">FAQ &nbsp;-&nbsp; Sitemap &nbsp;-&nbsp; Privacy Policy</span>
</div>

</body>
</html>
```